Business Card Design Project

In addition to the logo design we want a professional and contemporary business card for a talent management agency. We provide management services to creative artists and want to communicate a professional creative vibe.
Updates

Project Deadline Extended
Reason: Sorry didnt realise I had put such a short timeline on it.

Target Market(s)

The business deals with creative artists and other industry professionals

Industry/Entity Type

Artists

Colors

Designer to choose colors to be used in the design.

Requirements
Must have
• Logo
Address
Phone
Email

```html
<!DOCTYPE html>
<html lang="en">
<head>
<meta charset="UTF-8">
<title>Northvale Talent – Business Card</title>
<link rel="stylesheet" href="https://fonts.googleapis.com/css2?family=Open+Sans:wght@400;700;800&display=swap">
<style>
  :root {
    --page-bg: #ebebeb;
    --card-black: #000000;
    --card-grey: #cfcfcf;
    --card-grey-light: #f2f2f2;
    --accent-blue: #159fd2;
    --ink-white: #ffffff;
    --ink-black: #111111;
    --ink-dark: #2b2b2b;
    --ink-muted: #5c5c5c;
    --watermark: rgba(0, 0, 0, 0.06);
  }
  * { box-sizing: border-box; margin: 0; padding: 0; }
  html, body {
    width: 1200px;
    height: 918px;
    overflow: hidden;
    background: var(--page-bg);
    font-family: "Open Sans", Arial, sans-serif;
  }
  .card-set {
    display: flex;
    gap: 60px;
    justify-content: center;
    align-items: center;
    width: 1200px;
    height: 918px;
  }
  .card {
    position: relative;
    width: 520px;
    height: 300px;
    overflow: hidden;
    box-shadow: 0 8px 24px rgba(0, 0, 0, 0.18);
  }

  /* Front */
  .card-front { background: var(--card-black); }
  .card-front .corner-block {
    position: absolute; left: 0; top: 0;
    width: 72px; height: 30px;
    background: var(--ink-white);
  }
  .card-front .top-band {
    position: absolute; left: 72px; top: 0;
    width: 320px; height: 18px;
    background: var(--accent-blue);
  }
  .company-name {
    position: absolute; left: 40px; bottom: 34px;
    color: var(--ink-white);
    font-weight: 400;
    font-size: 50px;
    line-height: 1;
    letter-spacing: -1px;
    white-space: nowrap;
  }

  /* Back */
  .card-back {
    background: radial-gradient(ellipse 55% 60% at 40% 45%, var(--card-grey-light), var(--card-grey));
  }
  .card-back .top-band {
    position: absolute; right: 0; top: 0;
    width: 250px; height: 26px;
    background: var(--accent-blue);
  }
  .card-back .corner-left {
    position: absolute; left: 0; top: 0;
    width: 80px; height: 26px;
    background: var(--ink-white);
  }
  .card-back .corner-left::after {
    content: ""; position: absolute; left: 0; top: 0;
    width: 80px; height: 12px; background: var(--accent-blue);
  }
  .card-back .corner-right {
    position: absolute; right: 0; bottom: 0;
    width: 80px; height: 26px;
    background: var(--ink-white);
  }
  .name-watermark {
    position: absolute; left: 140px; top: 20px;
    writing-mode: vertical-rl;
    font-weight: 800;
    font-size: 120px;
    line-height: 1;
    color: var(--watermark);
  }
  .person {
    position: absolute; left: 40px; top: 50px;
  }
  .person-name {
    font-weight: 700;
    font-size: 34px;
    letter-spacing: -1.5px;
    line-height: 1;
  }
  .person-name .first { color: var(--ink-black); }
  .person-name .last { color: var(--ink-dark); }
  .person-role {
    font-size: 14px;
    color: var(--ink-muted);
    text-align: right;
    margin-top: 2px;
  }
  .contact {
    position: absolute; right: 26px; bottom: 46px;
    list-style: none;
    font-size: 11px;
    line-height: 1.5;
    color: var(--ink-muted);
  }
</style>
</head>
<body>
  <main class="card-set">
    <section class="card card-front" aria-label="Card front">
      <div class="corner-block"></div>
      <div class="top-band"></div>
      <h1 class="company-name">Northvale Talent</h1>
    </section>

    <section class="card card-back" aria-label="Card back">
      <div class="corner-left"></div>
      <div class="top-band"></div>
      <div class="corner-right"></div>
      <div class="name-watermark" aria-hidden="true">sam</div>
      <div class="person">
        <h2 class="person-name"><span class="first">sam</span><span class="last">harlow</span></h2>
        <p class="person-role">Northvale Talent Owner</p>
      </div>
      <ul class="contact">
        <li>email • sam@northvale.com.au</li>
        <li>phone • 313 555 0148</li>
        <li>web • northvale.com.au</li>
      </ul>
    </section>
  </main>
</body>
</html>
```